New Wordpress Design Project: KV- Kindred Vantage, Training Beyond Equity, Diversity, and Inclusion

I need a clean, modern, website design for KV- a national consulting firm providing equity, diversity, and inclusion training, through the lens of undoing racism, for arts and culture, and the non profit industry. It will feature both written posts, and some video. People will need KV contact information, and subscribe to receive information. It will feature a pretty active blog, and a section for resources, with links to other sites. There needs to be a section about KV,its training, approach, and bio Information. I probably should have put this first!

I want a site that draws people in. That is interesting and dynamic. My approach to this work is to provide people with the information, knowledge, and tools they need to go back to their communities and do the work. So they are at the center of the story. And I like powerful imagery. It could also be pretty.

The idea of undoing racism is a big idea. It is powerful, heroic even. And thousands of people in the US are working hard to do just that. So there is a sense of movement building here, of connecting to something important.

I already have a logo design that was done through a contest here last month.

Target Market(s)

Arts and culture fields, non profit industry, and philanthropy

Font styles to use
Sans Serif

Requirements
Must have
• Must have dynamic powerful imagery, be clean and easy to navigate, support concept of story telling, good use of color, be inviting, draw people in to learn when they see it first time. The ability to update photos, and videos easily. Connect to social media, especially Facebook and LinkedIn.
Nice to have
• It would be nice to have a website that uses more images than words to tell stories. I don't know enough about what's possible in website design to add more to this section.
Should not have
• Should not look like we are selling products, or services even but, rather, providing essential information and knowledge to help people make this world a better place for more people.

```html
<!DOCTYPE html>
<html lang="en">
<head>
<meta charset="utf-8">
<title>Kindred Vantage</title>
<link rel="stylesheet" href="https://fonts.googleapis.com/css2?family=Lato:wght@400;700;900&family=Marcellus&family=Saira:wdth,wght@112.5,700&display=swap">
<style>
:root{
  --yellow:#ffdd00;
  --black:#0d0d0d;
  --dark:#333333;
  --light:#f2f2f2;
  --white:#ffffff;
  --text:#222222;
  --muted:#555555;
  --sky-top:#6fb2e6;
  --sky-bottom:#d6eaf7;
  --warm:#e08a50;
  --skin:#d9a883;
}
*{box-sizing:border-box;margin:0;padding:0}
html,body{width:1200px;height:2281px;overflow:hidden}
body{position:relative;font-family:"Lato",sans-serif;color:var(--text);background:var(--white)}
.abs{position:absolute}

/* header */
.topbar{left:0;top:0;width:1200px;height:99px;background:var(--black);color:var(--white)}
.contact-item{top:26px;display:flex;align-items:center;gap:14px;font-size:16px;line-height:1.25}
.contact-item b{display:block;font-weight:700}
.navbar{left:0;top:99px;width:1200px;height:41px;background:var(--yellow)}
.nav-link{top:0;height:41px;line-height:41px;font-size:15px;color:var(--text);text-align:center;width:120px}
.nav-link.active{font-weight:700}
.nav-sep{top:6px;width:1px;height:30px;background:rgba(0,0,0,.15)}
.brand-tab{left:494px;top:56px;width:212px;height:86px}
.brand{left:500px;top:88px;width:200px;text-align:center;color:var(--white);font-size:21px;font-weight:400;display:flex;align-items:center;justify-content:center;gap:8px}
.brand-dot{width:14px;height:14px;border-radius:50%;background:var(--yellow)}

/* hero */
.hero{left:0;top:140px;width:1200px;height:525px;
  background:
    radial-gradient(ellipse 380px 170px at 50% 230px, rgba(224,138,80,.55), rgba(224,138,80,0) 100%),
    linear-gradient(90deg, rgba(217,168,131,.6) 0%, rgba(217,168,131,0) 22%, rgba(217,168,131,0) 78%, rgba(217,168,131,.6) 100%),
    linear-gradient(180deg,var(--sky-top),var(--sky-bottom))}
.hero-caption{left:0;top:499px;width:1200px;height:90px;background:rgba(50,50,50,.6);color:var(--white);font-family:"Saira",sans-serif;font-stretch:112.5%;font-weight:700;font-size:26px;text-align:center;line-height:33px;padding-top:12px}
.dots{left:566px;top:605px;display:flex;gap:8px}
.dots span{width:16px;height:16px;border-radius:50%;border:2px solid var(--black);background:var(--white)}
.dots span.on{background:var(--yellow)}

/* features */
.features{left:0;top:665px;width:1200px;height:181px}
.feature{top:0;width:420px;text-align:center}
.feature h3{font-family:"Marcellus",serif;font-weight:400;font-size:25px;margin-top:55px}
.feature p{font-size:12.5px;line-height:19px;margin-top:10px;padding:0 20px}
.feature .plus{display:inline-block;width:24px;height:24px;line-height:24px;font-weight:900;font-size:17px;margin-top:10px;border-radius:2px}
.feature-icon{width:70px;height:70px;border-radius:50%;display:flex;align-items:center;justify-content:center}
.center-badge{left:538px;top:712px;width:112px;height:82px;border-radius:50%;background:var(--white);border:5px solid var(--yellow);display:flex;align-items:center;justify-content:center;font-size:30px;color:var(--black)}

/* welcome */
.welcome{left:0;top:846px;width:1200px;height:363px;background:var(--light)}
.welcome h2{left:100px;top:50px;font-family:"Marcellus",serif;font-weight:400;font-size:29px;color:var(--black)}
.rule{height:2px;background:#444}
.lead{left:100px;top:116px;width:640px;font-size:16.5px;font-weight:700;line-height:25px;color:var(--black)}
.body-copy{left:100px;top:180px;width:640px;font-size:13px;line-height:21px;color:var(--muted)}
.pill{border-radius:22px;font-weight:700;font-size:15px;text-align:center}
.video{left:802px;top:88px;width:301px;height:222px;border-radius:4px;overflow:hidden;box-shadow:0 8px 14px rgba(0,0,0,.25)}
.video-frame{position:absolute;left:0;top:0;width:301px;height:192px;background:linear-gradient(135deg,#dfe6ea,#8a97a3)}
.video-bar{position:absolute;left:0;top:192px;width:301px;height:30px;background:linear-gradient(#3a3a3a,#151515)}

/* objective */
.objective{left:0;top:1209px;width:1200px;height:221px;background:var(--yellow);text-align:center}
.objective h2{font-family:"Marcellus",serif;font-weight:400;font-size:28px;line-height:42px;color:var(--black);margin-top:36px}

/* inquiry */
.inquiry{left:0;top:1430px;width:1200px;height:191px;background:repeating-linear-gradient(45deg,#111 0 3px,#1c1c1c 3px 6px)}
.inquiry h2{top:30px;left:0;width:1200px;text-align:center;font-family:"Marcellus",serif;font-weight:400;font-size:28px;color:var(--white)}
.field{top:102px;height:45px;background:var(--white);border-radius:2px;font-size:13px;color:#333;padding:14px 12px}
.submit{left:922px;top:102px;width:181px;height:45px;background:var(--yellow);font-size:19px;text-align:center;line-height:45px;color:var(--black);border-radius:2px}

/* blog */
.section-title{font-family:"Marcellus",serif;font-size:27px;color:var(--black);display:flex;align-items:center;gap:12px}
.arrows{font-size:20px;color:#555;letter-spacing:4px}
.post-thumb{width:116px;height:91px;background:linear-gradient(135deg,#c9d8e6,#5d7ea1)}
.post h4{font-size:15px;font-weight:700;color:var(--black)}
.post p{font-size:12.5px;line-height:20px;color:#444;margin-top:6px}
.meta{font-size:12.5px;color:#444;margin-top:10px;display:flex;gap:30px}
.meta span::before{content:"";display:inline-block;width:9px;height:9px;border:2px solid #e6b800;border-radius:50%;margin-right:8px;vertical-align:-1px}
.recent{left:640px;width:463px;display:flex;gap:16px;align-items:flex-start}
.recent p{font-size:12.5px;line-height:18px;color:#333}

/* footer */
.footer{left:0;top:2000px;width:1200px;height:236px;background:var(--dark);color:var(--white)}
.footer h5{font-size:14.5px;font-weight:700;padding-bottom:8px;border-bottom:1px solid #555}
.footer ul{list-style:none;margin-top:14px}
.footer li{font-size:12.5px;line-height:23.5px;color:#ddd}
.footer li::before{content:"\2192";color:var(--yellow);margin-right:10px}
.footer li.current{color:var(--yellow)}
.fdiv{top:32px;width:1px;height:176px;background:#555}
.fsmall{font-size:12px;line-height:17px;color:#ddd}
.footer-brand{left:870px;top:100px;width:250px;display:flex;align-items:center;justify-content:center;gap:10px;font-size:29px;color:var(--white)}
.copyright{left:0;top:2236px;width:1200px;height:45px;background:var(--black);color:#ddd;font-size:12px;text-align:center;line-height:45px}
</style>
</head>
<body>

<header>
  <div class="abs topbar">
    <div class="abs contact-item" style="left:100px">
      <svg width="36" height="40" viewBox="0 0 36 40" aria-hidden="true"><path d="M10 4 C4 8 3 18 10 28 C17 38 26 38 31 34 L26 27 L21 30 C17 27 14 22 13 17 L18 14 L14 5 Z" fill="none" stroke="#ffdd00" stroke-width="3"/></svg>
      <div><b>Call Us:</b>123 456 7890</div>
    </div>
    <div class="abs contact-item" style="left:858px">
      <svg width="38" height="34" viewBox="0 0 38 34" aria-hidden="true"><path d="M3 10 L28 3 L35 26 L10 33 Z M3 10 L22 20 L28 3" fill="none" stroke="#ffdd00" stroke-width="3" stroke-linejoin="round"/></svg>
      <div><b>Mail Us:</b>inquiry@kindredvantage.com</div>
    </div>
  </div>
  <nav class="abs navbar">
    <div class="abs nav-link active" style="left:95px">Home</div>
    <div class="abs nav-sep" style="left:206px"></div>
    <div class="abs nav-link" style="left:214px">About Us</div>
    <div class="abs nav-sep" style="left:336px"></div>
    <div class="abs nav-link" style="left:339px">Services</div>
    <div class="abs nav-link" style="left:731px">Blog Posts</div>
    <div class="abs nav-sep" style="left:864px"></div>
    <div class="abs nav-link" style="left:865px">Gallery</div>
    <div class="abs nav-sep" style="left:986px"></div>
    <div class="abs nav-link" style="left:1000px">Contact Us</div>
  </nav>
  <svg class="abs brand-tab" viewBox="0 0 212 86" aria-hidden="true"><path d="M0 43 L0 0 L212 0 L212 43 C200 43 196 86 176 86 L36 86 C16 86 12 43 0 43 Z" fill="#0d0d0d"/></svg>
  <div class="abs brand"><span class="brand-dot"></span>Kindred Vantage</div>
</header>

<section class="abs hero" role="img" aria-label="Two hands holding a chain of paper people in many skin tones, from light to dark, against a bright blue cloudy sky"></section>
<div class="abs hero-caption">WE ARE A NATIONAL FIRM PROVIDING EQUITY AND INCLUSION<br>TRAINING</div>
<div class="abs dots"><span></span><span class="on"></span><span></span></div>

<section class="abs features">
  <svg class="abs" style="left:0;top:0" width="1200" height="181" viewBox="0 0 1200 181" aria-hidden="true">
    <rect width="1200" height="181" fill="#ffdd00"/>
    <polygon points="0,0 617,0 553,181 0,181" fill="#333333"/>
    <polygon points="610,0 620,0 560,181 550,181" fill="#ffffff"/>
  </svg>
  <div class="abs feature" style="left:73px;color:#fff">
    <h3>Training</h3>
    <p>Lorem ipsum dolor sit amet, consectetuer adipiscing elit, sed diam nonummy nibh euismod tincidunt ut laoreet</p>
    <span class="plus" style="background:var(--yellow);color:var(--black)">+</span>
  </div>
  <div class="abs feature" style="left:670px;color:var(--black)">
    <h3>Approach</h3>
    <p>Lorem ipsum dolor sit amet, consectetuer adipiscing elit, sed diam nonummy nibh euismod tincidunt ut laoreet</p>
    <span class="plus" style="background:var(--dark);color:var(--yellow)">+</span>
  </div>
</section>
<div class="abs feature-icon" style="left:248px;top:633px;background:var(--yellow)">
  <svg width="34" height="30" viewBox="0 0 34 30" aria-hidden="true"><rect x="9" y="2" width="18" height="12" fill="none" stroke="#222" stroke-width="2.5"/><circle cx="6" cy="20" r="4" fill="#222"/><circle cx="17" cy="20" r="4" fill="#222"/><circle cx="28" cy="20" r="4" fill="#222"/><rect x="1" y="25" width="32" height="5" rx="2" fill="#222"/></svg>
</div>
<div class="abs feature-icon" style="left:845px;top:633px;background:var(--dark)">
  <svg width="32" height="32" viewBox="0 0 32 32" aria-hidden="true"><path d="M16 30 V17 L6 8 M16 17 L26 8 M3 4 H10 V11 M29 4 H22 V11" fill="none" stroke="#ffdd00" stroke-width="3"/></svg>
</div>
<div class="abs center-badge">KV</div>

<section class="abs welcome">
  <h2 class="abs">Welcome To Kindred Vantage</h2>
  <div class="abs rule" style="left:100px;top:96px;width:640px"></div>
  <p class="abs lead">Lorem ipsum dolor sit amet, consectetuer adipiscing elit, sed diam nonummy nibh euismod tincidunt ut laoreet dolore magna aliquam erat volutpat.</p>
  <p class="abs body-copy">Lorem ipsum dolor sit amet, consectetuer adipiscing elit, sed diam nonummy nibh euismod tincidunt uterr laoreet dolore magna aliquam erat volutpat. Ut wisi enim ad minim veniam, quis nostrud exerci tationerwi laoreet dolore magna aliquam erati volutpat. Ut wisi enim ad minim veniam, quis nostrud exerci iationweri ullamcorpererer suscipit lobortis nisl uterr aliquip ex ea commodo consequat.</p>
  <div class="abs pill" style="left:98px;top:278px;width:132px;height:40px;line-height:40px;background:var(--yellow);color:var(--black)">Read More</div>
  <div class="abs video">
    <div class="video-frame" role="img" aria-label="Video still of three colleagues shaking hands at a meeting table"></div>
    <svg class="abs" style="left:128px;top:78px" width="48" height="34" viewBox="0 0 48 34" aria-hidden="true"><rect width="48" height="34" rx="7" fill="#111"/><polygon points="19,9 32,17 19,25" fill="#fff"/></svg>
    <div class="video-bar">
      <svg class="abs" style="left:10px;top:10px" width="280" height="12" viewBox="0 0 280 12" aria-hidden="true"><polygon points="0,4 4,4 9,0 9,12 4,8 0,8" fill="#ccc"/><rect x="18" y="4" width="170" height="4" rx="2" fill="#555"/><rect x="18" y="4" width="78" height="4" rx="2" fill="#d11"/><path d="M270 1 L278 1 L278 9 M270 11 L262 11 L262 3" fill="none" stroke="#ccc" stroke-width="2"/></svg>
    </div>
  </div>
</section>

<section class="abs objective">
  <h2>Our Objective Is To Maintain A Culture of Mutual Respect And Consideration,<br>Ensuring That Everyone Is Treated Equally</h2>
  <div class="abs pill" style="left:508px;top:146px;width:127px;height:36px;line-height:36px;background:var(--black);color:var(--white)">Get Started</div>
</section>

<section class="abs inquiry">
  <h2 class="abs">Quick Inquiry</h2>
  <div class="abs field" style="left:100px;width:224px">Name</div>
  <div class="abs field" style="left:347px;width:223px">Email</div>
  <div class="abs field" style="left:593px;width:306px">Message</div>
  <div class="abs submit">Get Started</div>
</section>

<section class="abs" style="left:0;top:1621px;width:1200px;height:379px">
  <div class="abs section-title" style="left:100px;top:40px">
    <svg width="34" height="26" viewBox="0 0 34 26" aria-hidden="true"><ellipse cx="14" cy="10" rx="13" ry="9" fill="#ffdd00"/><path d="M6 16 L3 24 L13 18 Z" fill="#ffdd00"/></svg>
    Latest Blog
  </div>
  <div class="abs arrows" style="left:535px;top:48px">‹›</div>
  <div class="abs rule" style="left:100px;top:90px;width:463px;background:#ccc"></div>
  <div class="abs rule" style="left:100px;top:90px;width:140px;background:var(--yellow)"></div>

  <div class="abs post-thumb" style="left:100px;top:113px" role="img" aria-label="Hands reviewing financial charts on paper"></div>
  <div class="abs post" style="left:246px;top:111px;width:320px">
    <h4>Ut wisi enim ad minim veniam, quiswerer</h4>
    <p>Lorem ipsum dolor sit amet, consectetuer adipcing elit, sed diam nonummy nibh ...[+]</p>
    <div class="meta"><span>3:50 Pm</span><span>Dec 10, 2016</span></div>
  </div>
  <div class="abs post-thumb" style="left:100px;top:235px" role="img" aria-label="Business colleagues shaking hands"></div>
  <div class="abs post" style="left:246px;top:233px;width:320px">
    <h4>Ut wisi enim ad minim veniam, quiswerer</h4>
    <p>Lorem ipsum dolor sit amet, consectetuer adipcing elit, sed diam nonummy nibh ...[+]</p>
    <div class="meta"><span>3:50 Pm</span><span>Dec 10, 2016</span></div>
  </div>

  <div class="abs section-title" style="left:646px;top:42px">
    <svg width="28" height="24" viewBox="0 0 28 24" aria-hidden="true"><rect x="1" y="6" width="26" height="17" fill="#222"/><path d="M1 6 L14 16 L27 6" fill="none" stroke="#fff" stroke-width="2"/><path d="M4 0 L10 4" stroke="#ffdd00" stroke-width="3"/></svg>
    Recent Posts
  </div>
  <div class="abs arrows" style="left:1075px;top:48px">‹›</div>
  <div class="abs rule" style="left:640px;top:90px;width:463px;background:#ccc"></div>
  <div class="abs rule" style="left:640px;top:90px;width:120px;background:var(--yellow)"></div>

  <div class="abs recent" style="top:107px"><svg width="26" height="30" viewBox="0 0 26 30" aria-hidden="true"><path d="M4 26 L7 18 L20 3 L24 7 L11 22 Z M4 26 L11 22" fill="none" stroke="#222" stroke-width="2.5"/></svg><p>Lorem ipsum dolor sit amet, consectetuer adipiscing elit, sed diam no nummy nibh euismod tincidunt uterr laoreet dolore</p></div>
  <div class="abs recent" style="top:165px"><svg width="26" height="30" viewBox="0 0 26 30" aria-hidden="true"><path d="M4 26 L7 18 L20 3 L24 7 L11 22 Z M4 26 L11 22" fill="none" stroke="#222" stroke-width="2.5"/></svg><p>Lorem ipsum dolor sit amet, consectetuer adipiscing elit, sed diam no nummy nibh euismod tincidunt uterr laoreet dolore</p></div>
  <div class="abs recent" style="top:223px"><svg width="26" height="30" viewBox="0 0 26 30" aria-hidden="true"><path d="M4 26 L7 18 L20 3 L24 7 L11 22 Z M4 26 L11 22" fill="none" stroke="#222" stroke-width="2.5"/></svg><p>Lorem ipsum dolor sit amet, consectetuer adipiscing elit, sed diam no nummy nibh euismod tincidunt uterr laoreet dolore</p></div>
  <div class="abs recent" style="top:281px"><svg width="26" height="30" viewBox="0 0 26 30" aria-hidden="true"><path d="M4 26 L7 18 L20 3 L24 7 L11 22 Z M4 26 L11 22" fill="none" stroke="#222" stroke-width="2.5"/></svg><p>Lorem ipsum dolor sit amet, consectetuer adipiscing elit, sed diam no nummy nibh euismod tincidunt uterr laoreet dolore</p></div>
</section>

<footer class="abs footer">
  <div class="abs" style="left:100px;top:30px;width:100px">
    <h5>Quick Links</h5>
    <ul>
      <li class="current">Home</li><li>About Us</li><li>Services</li><li>Blog Posts</li><li>Gallery</li><li>Contact Us</li>
    </ul>
  </div>
  <div class="abs fdiv" style="left:274px"></div>
  <div class="abs" style="left:306px;top:30px;width:175px">
    <h5>Contact Detail</h5>
    <p class="fsmall" style="margin-top:14px"><b>KV Firm</b><br>16 Lorem ipsum dolor sit amet<br>sed benetion, Street no-123456</p>
    <p class="fsmall" style="margin-top:12px;line-height:23px">&#9742;&nbsp; 123-456-1789<br>&#9743;&nbsp; 123-456-1789<br><span style="color:var(--yellow)">&#9993;</span>&nbsp; inquiry@kvfirm.com</p>
  </div>
  <div class="abs fdiv" style="left:531px"></div>
  <div class="abs" style="left:586px;top:30px;width:190px">
    <h5>Newsletter Signup</h5>
    <p class="fsmall" style="margin-top:14px">Get latest updates by entering your email address</p>
    <div style="margin-top:12px;width:190px;height:25px;background:#fff;border-radius:3px;color:#333;font-size:11px;font-weight:700;padding:6px 6px">Email Address</div>
    <div style="margin-top:10px;width:104px;height:26px;background:var(--yellow);color:var(--black);font-size:12.5px;font-weight:700;text-align:center;line-height:26px;border-radius:2px">SUBSCRIBE</div>
  </div>
  <div class="abs fdiv" style="left:829px"></div>
  <div class="abs footer-brand"><span class="brand-dot" style="width:16px;height:16px"></span>Kindred Vantage</div>
</footer>
<div class="abs copyright">Copyright © 2017 KVfirm. All Rights Reserved.</div>

</body>
</html>
```